Complete web site needs re-design

Webpage will include one product labeled Talvex (™) .
This webpage must be viewable on Mobile devices and all common browsers - Safari, Chrome, IE, Mozilla Firefox..

Design will be similar to that of
http://www.morvellworks.example/aviation/
or
http://www.plexory.example/site-layout/view/html/482?utm_content=qx_html_ktp_demo_3_7TrialItem&utm_medium=layout_strip&utm_campaign=qx_ktp&utm_source=opensitelayouts&experiment_id=qx_html_ktp_demo_3_7TrialItem&utm_term=meetups

- in that it will be simple and introduce our product.

Website will be ready to accept shop till when the product is released. The integration of this feature will also go to the winner.

Tabs for information will be provided for "About, Features, Where to buy"

The page should include one vidqueue as a sample of the product. this will be linked to the following video http://www.vidqueue.example/watch?v=kRT519pz8va.

Good luck applicants!

Target Market(s)

The target audience will be sport enthusiasts of all walks (from car racing to skydiving) looking to supplement their zip-cam camera with an extra mount.

Industry/Entity Type

Events

Font styles to use
Other font styles liked:
• Helvetica

Colors
d5d5d5
919191
f6f6f6
c8c8c8
ebebeb
5c5c5c
aaaaaa
ffffff

Requirements
Must have
• Front page is introducing our "Talvex" product. Search engines need to identify "Extreme, POV, ZipCam, Self,Levelling, Auto, Stabilising, Motocross, surfing, Moto X, Wake, Kite, Boarding, Skydiving, Racing, Bike, Aerobatic, blue stag, Mount,Ski, downhill, snow, base jumping," etc..

The mount is designed to hold a zip-cam camera in all and any extreme situations. Ensure the search returns this .

An "about" and "contact" shall be provided on the company logo.

Tabs for information will be provided for "About, Features, Where to buy" - This information will be provided by us, once the webpage is complete.

Font is "Helvetica"
Nice to have
• Prepare the page flow so multiple variations of the product, and accessories can be added easily. As mentioned earlier, a shopping cart will be required (ShopTill) in the near future.

As you can see the company logo is designed to be cut into the product. It would be nice if it had an embossed effect to look the same. This goes for the "Talvex" logo also.

```html
<!DOCTYPE html>
<html lang="en">
<head>
<meta charset="utf-8">
<title>Talvex – SkyVane KX7</title>
<link rel="stylesheet" href="https://fonts.googleapis.com/css2?family=Open+Sans:wght@400;600;700&display=swap">
<style>
  :root {
    --page-bg: #ebebeb;
    --topbar-bg: #f6f6f6;
    --topbar-text: #333333;
    --nav-bg: #5ab4d8;
    --nav-text: #ffffff;
    --brand-text: #1f2d36;
    --frame-bg: #d5d5d5;
    --hero-light: #c8c8c8;
    --hero-mid: #aaaaaa;
    --hero-dark: #919191;
    --headline: #2a2a2a;
    --tagline: #1f4a6e;
  }
  * { box-sizing: border-box; margin: 0; padding: 0; }
  html, body {
    width: 1200px;
    height: 610px;
    overflow: hidden;
    background: var(--page-bg);
    font-family: "Open Sans", Helvetica, Arial, sans-serif;
  }
  .site {
    width: 1200px;
    height: 610px;
    display: flex;
    flex-direction: column;
  }
  .account-bar {
    height: 37px;
    background: var(--topbar-bg);
    display: flex;
    justify-content: flex-end;
    align-items: center;
    gap: 20px;
    padding-right: 22px;
    font-size: 14px;
    font-weight: 600;
    color: var(--topbar-text);
  }
  .main-nav {
    height: 46px;
    background: var(--nav-bg);
    display: flex;
    align-items: center;
    padding-left: 44px;
    gap: 30px;
  }
  .brand {
    font-size: 17px;
    font-weight: 700;
    color: var(--brand-text);
    margin-right: 14px;
  }
  .nav-link {
    display: flex;
    align-items: center;
    gap: 5px;
    font-size: 13px;
    font-weight: 600;
    color: var(--nav-text);
  }
  .nav-icon { width: 12px; height: 12px; fill: var(--nav-text); }
  .content {
    flex: 1;
    background: var(--frame-bg);
    padding: 22px 20px 0;
  }
  .hero {
    position: relative;
    height: 100%;
    background: radial-gradient(ellipse at 50% 30%, var(--hero-light) 0%, var(--hero-mid) 60%, var(--hero-dark) 100%);
    text-align: center;
    padding-top: 38px;
  }
  .hero-title {
    font-size: 50px;
    font-weight: 400;
    color: var(--headline);
    line-height: 1.1;
  }
  .hero-tagline {
    font-size: 29px;
    font-weight: 400;
    color: var(--tagline);
    margin-top: 4px;
  }
  .product-visual {
    position: absolute;
    left: 50%;
    transform: translateX(-50%);
    top: 215px;
    width: 800px;
    height: 240px;
    background: radial-gradient(ellipse at 50% 55%, #5c5c5c 0%, #919191 45%, rgba(170,170,170,0) 75%);
  }
</style>
</head>
<body>
<div class="site">
  <header class="account-bar">
    <span class="account-link">Log in</span>
    <span class="account-link">Cart</span>
  </header>
  <nav class="main-nav">
    <span class="brand">Talvex</span>
    <span class="nav-link">
      <svg class="nav-icon" viewBox="0 0 12 12"><path d="M6 1 L11 6 H9.5 V11 H7 V8 H5 V11 H2.5 V6 H1 Z"/></svg>Home
    </span>
    <span class="nav-link">
      <svg class="nav-icon" viewBox="0 0 12 12"><circle cx="6" cy="3.5" r="2.5"/><path d="M1 11 C1 7 11 7 11 11 Z"/></svg>About
    </span>
    <span class="nav-link">
      <svg class="nav-icon" viewBox="0 0 12 12"><path d="M6 1 L10.5 2.5 V6 C10.5 8.5 8.5 10.3 6 11 C3.5 10.3 1.5 8.5 1.5 6 V2.5 Z"/></svg>Features
    </span>
    <span class="nav-link">
      <svg class="nav-icon" viewBox="0 0 12 12"><circle cx="6" cy="2" r="1.3"/><rect x="4.8" y="4.3" width="2.4" height="6.7"/></svg>Where to buy
    </span>
    <span class="nav-link">
      <svg class="nav-icon" viewBox="0 0 12 12"><path d="M2.5 1 L4.5 1 L5.3 3.8 L4 4.8 C4.7 6.4 5.6 7.3 7.2 8 L8.2 6.7 L11 7.5 V9.5 C11 10.3 10.3 11 9.5 11 C5 11 1 7 1 2.5 C1 1.7 1.7 1 2.5 1 Z"/></svg>Contact us
    </span>
  </nav>
  <main class="content">
    <section class="hero">
      <h1 class="hero-title">SkyVane KX7</h1>
      <p class="hero-tagline">Beautiful. Functional. Brilliant</p>
      <div class="product-visual" role="img" aria-label="Photo of the black four-rotor drone with orange motors on a soft grey studio background"></div>
    </section>
  </main>
</div>
</body>
</html>
```